Elegant Black Candle Label Design!

I need a 2.375" tall by 3.0" wide candle label design. I'm looking for simple and elegant. Black label with silver leaf border and lettering. Label needs to have the following information on it: Fern Hollow Candle Co. as the company name, scent name in the middle and in smaller font, it needs to say Made in USA, All Natural, 8oz. Attached photos are for inspiration.

Target Market(s)

People looking for high end, all natural candle fragrances

Industry/Entity Type

Candle-Spa

Colors

Designer to choose only greyscale colors for use in the design.

Requirements
Must have
• Company Name, Scent (ability to change scent names), All Natural, Made in USA, 8oz
Nice to have
• Black background, silver leaf border and silver leaf font. Elegant fonts maybe slightly cursive

```html
<!DOCTYPE html>
<html lang="en">
<head>
<meta charset="utf-8">
<title>Fern Hollow Candle Co. – Sandalwood Label</title>
<link rel="stylesheet" href="https://fonts.googleapis.com/css2?family=Montserrat:wght@400;700&family=Playfair+Display:wght@700&display=swap">
<style>
  :root {
    --canvas-bg: #1b1c1f;
    --label-black: #000000;
    --label-sheen: #2f2f2f;
    --label-mid: #121212;
    --silver-dark: #6e6e6e;
    --silver-light: #e6e6e6;
    --silver-text: #bdbdbd;
    --white: #ffffff;
  }
  * { margin: 0; padding: 0; box-sizing: border-box; }
  html, body {
    width: 1200px;
    height: 1119px;
    overflow: hidden;
    background: var(--canvas-bg);
  }
  .label {
    position: absolute;
    left: 50px;
    top: 126px;
    width: 1100px;
    height: 866px;
    background: linear-gradient(90deg,
      var(--label-black) 0%,
      var(--label-mid) 30%,
      var(--label-sheen) 47%,
      var(--label-mid) 62%,
      var(--label-black) 86%);
  }
  .label__frame {
    position: absolute;
    inset: 8px;
    border: 6px solid;
    border-image: linear-gradient(90deg,
      var(--silver-dark) 0%,
      var(--silver-light) 25%,
      var(--silver-dark) 45%,
      var(--silver-light) 55%,
      var(--silver-dark) 75%,
      var(--silver-light) 100%) 1;
  }
  .brand {
    position: absolute;
    left: 0;
    right: 0;
    top: 78px;
    text-align: center;
    font-family: "Montserrat", sans-serif;
    font-weight: 400;
    color: var(--silver-text);
  }
  .brand__name {
    display: block;
    font-size: 74px;
    letter-spacing: 0.04em;
    line-height: 1.1;
  }
  .brand__suffix {
    display: block;
    margin-top: 14px;
    font-size: 30px;
    letter-spacing: 0.35em;
    line-height: 1;
  }
  .scent {
    position: absolute;
    left: 0;
    right: 0;
    top: 404px;
    text-align: center;
    font-family: "Playfair Display", serif;
    font-weight: 700;
    font-size: 106px;
    letter-spacing: 0.07em;
    line-height: 1;
    background: linear-gradient(90deg,
      #8a8a8a 0%, #d8d8d8 20%, #8f8f8f 40%, #f0f0f0 58%, #9a9a9a 78%, #cfcfcf 100%);
    -webkit-background-clip: text;
    background-clip: text;
    color: transparent;
  }
  .claims {
    position: absolute;
    left: 213px;
    top: 695px;
    width: 659px;
    height: 98px;
    display: flex;
    border: 2px solid var(--silver-light);
    font-family: "Montserrat", sans-serif;
    font-weight: 400;
    font-size: 36px;
    letter-spacing: 0.1em;
    color: var(--silver-text);
  }
  .claims__item {
    display: flex;
    align-items: center;
    justify-content: center;
    white-space: nowrap;
  }
  .claims__item--origin { width: 353px; border-right: 2px solid var(--silver-light); }
  .claims__item--natural { flex: 1; }
  .claims strong { font-weight: 700; margin-left: 0.3em; }
  .size {
    position: absolute;
    left: 930px;
    top: 706px;
    font-family: "Montserrat", sans-serif;
    font-weight: 400;
    color: var(--white);
    line-height: 1;
  }
  .size__value { font-size: 74px; }
  .size__unit { font-size: 40px; }
</style>
</head>
<body>
  <main class="label">
    <div class="label__frame"></div>
    <h1 class="brand">
      <span class="brand__name">Fern Hollow</span>
      <span class="brand__suffix">Candle Co.</span>
    </h1>
    <h2 class="scent">SANDALWOOD</h2>
    <div class="claims">
      <span class="claims__item claims__item--origin">Made in<strong>USA</strong></span>
      <span class="claims__item claims__item--natural">All Natural</span>
    </div>
    <p class="size"><span class="size__value">8</span><span class="size__unit">oz</span></p>
  </main>
</body>
</html>
```